Manuka honey jar label for new Manuka brand

We are planning to start a Manuka honey brand and we need to design the label for the honey jar. Manuka honey is an up and coming product and the market is still young in our country.
Our market is dominated by 1 brand: Orvana Health (photo attached). To the people who know what Manuka honey is, they associate it with Orvana Health in the same way people associate Cola with Zindle Pop or printer copies with Quorvix.
The good news is that a lot of people do not know yet what Manuka honey is and we still have the opportunity of being the first brand they get to know. At the same time, we still need to be able to take at least a bite out of the Orvana Health market share.
The Orvana Health label for their jar I think is not just absolutely gorgeous but it also does its job extremely well. It only features 3 informations:
- name of brand/logo (Orvana Health)
- name of product (Manuka Honey)
- and mgo rating which is like a rating of how strong the honey is
By having just this information on a relatively small label, their label SCREAMS Manuka by having the Manuka words twice (the brand and the product name) and people develop this association between Orvana Health and Manuka products in general.
Our product will also be in a similar square plastic jar. It will also be dark tinted, that´s important to note. We can also go for a blue cap but in order to differentiate ourselves from Orvana Health we thought of maybe choosing a black lid instead. I uploaded 2 jars, 1 with black lid and 1 with gold (although it looks more like mustard) that you can use for simulations. They are pretty accurate of the type of jars and lids that we can have.
The label has total length of about 20cm. One side of the jar has 5,5 cm of the label and the height of the label is 4,5 cm. We can also use selective gold laminating on the label but we cannot have custom shape label at this point as Orvana Health does with its tree logo that sticks outside the label.
I need the design for the entire label but the focus should be on the front part, that is the part that sells and catches your eye. Like Orvana Health, the front part I want to have 3 vital informations:
- name of brand/logo (in our case Velmora Botanica) - we do not have a pre-existing logo, this needs to be created alongside the label
- and mgo rating
As "other" information we also need the net weight "250 g" alongside with the typical "e" to appear on the front. That is a legal requirement.
Optionally, you can add a small phrase somewhere like "Harvested in New Zealand" or "Made in New Zealand" since this is a product that is only made there and in some areas of Australia.
This is pretty much all the info. As a final note, there are a ton of beautiful premium Manuka honey jar labels. But they are too fancy and when you look at them you don´t instantly recognize that it is Manuka Honey.
This instant recognition is vital! With this small jar there is the danger for customers to think that maybe it´s medicine, maybe it´s sports supplements etc. This is a relatively small product and imagine you just glance on it on the retail shelf. Instantly you must think it is Manuka Honey and that it is beautiful. And if you see it on the shelf next to Orvana Health, it would be best to also think that you would rather buy this (it gives you more trust) than the Orvana Health.
One final note: I do not want the bee as an insect on the label. I think some people are turned off when they see an insect with its small legs and make a bad association that there are insects inside. I do not mind symbolism or somehow super stylized bee in a modern way, but I do not want a plain insect on the label.
For any other questions, I am at your disposal. Thank you very much for taking the time to send us a proposal!

```html
<!DOCTYPE html>
<html lang="en">
<head>
<meta charset="utf-8">
<title>Velmora Botanica – Manuka Honey Label</title>
<link href="https://fonts.googleapis.com/css2?family=Cinzel:wght@700&family=Poppins:wght@500;600;700&display=swap" rel="stylesheet">
<style>
  :root {
    --page-bg: #e9e9e9;
    --honey-light: #ffe21a;
    --honey-mid: #fbb417;
    --honey-deep: #ef8a22;
    --ink: #151010;
    --maroon: #5e1010;
    --glow: #ffe44a;
    --silver-dark: #9a9a9a;
    --silver-light: #f4f4f4;
    --leaf: #1f8a3c;
    --pill: #111111;
    --white: #ffffff;
  }
  * { margin: 0; padding: 0; box-sizing: border-box; }
  html, body { width: 1200px; height: 939px; overflow: hidden; }
  body { background: var(--page-bg); position: relative; }

  .label {
    position: absolute;
    left: 100px; top: 60px;
    width: 1000px; height: 820px;
    overflow: hidden;
    text-align: center;
    color: var(--ink);
  }
  .label__field {
    position: absolute; inset: 0;
    background: radial-gradient(ellipse 60% 55% at 50% 22%, var(--honey-light) 0%, var(--honey-mid) 45%, var(--honey-deep) 100%);
  }
  .label__band {
    position: absolute; left: 0; width: 100%; height: 28px;
    background: linear-gradient(90deg, var(--silver-dark), var(--silver-light) 30%, #cfcfcf 55%, var(--silver-light) 80%, var(--silver-dark));
  }
  .label__band--top { top: 0; }
  .label__band--bottom { bottom: 0; }

  .brand-mark {
    position: absolute; left: 50%; top: 78px;
    width: 78px; height: 78px; margin-left: -39px;
    border-radius: 50%;
    background: var(--leaf);
  }
  .brand-name {
    position: absolute; left: 0; right: 0; top: 200px;
    font-family: "Cinzel", serif; font-weight: 700;
    font-size: 52px; letter-spacing: 0.5px; line-height: 1;
  }
  .origin {
    position: absolute; left: 0; right: 0; top: 262px;
    font-family: "Poppins", sans-serif; font-weight: 500;
    font-size: 35px; line-height: 1;
  }
  .divider {
    position: absolute; left: 50%; top: 338px;
    width: 172px; height: 5px; margin-left: -86px;
    background: var(--ink);
  }
  .product-name {
    position: absolute; left: 0; right: 0;
    font-family: "Cinzel", serif; font-weight: 700;
    color: var(--maroon);
    text-shadow: 0 0 3px var(--glow), 0 0 3px var(--glow);
    line-height: 1;
  }
  .product-name--first { top: 392px; font-size: 66px; }
  .product-name--second { top: 452px; font-size: 120px; }

  .grade {
    position: absolute; left: 50%; top: 598px;
    width: 246px; height: 60px; margin-left: -123px;
    background: var(--pill);
    border-radius: 26px 8px 26px 8px;
    color: var(--white);
    font-family: "Poppins", sans-serif; font-weight: 700;
    font-size: 40px; line-height: 60px;
  }
  .net-weight {
    position: absolute; left: 0; right: 0; top: 718px;
    font-family: "Poppins", sans-serif; font-weight: 500;
    font-size: 35px; line-height: 1;
  }
  .net-weight__small { font-size: 26px; }
</style>
</head>
<body>
  <section class="label">
    <div class="label__field" role="img" aria-label="Honey-orange gradient with honeycomb hexagon pattern"></div>
    <div class="label__band label__band--top"></div>

    <div class="brand-mark"></div>
    <h1 class="brand-name">VELMORA BOTANICA</h1>
    <p class="origin">Made in New Zealand</p>
    <div class="divider"></div>

    <p class="product-name product-name--first">MANUKA</p>
    <p class="product-name product-name--second">HONEY</p>

    <div class="grade">MGO 250</div>
    <p class="net-weight">NET <span class="net-weight__small">WT.</span> 9oz (250g)</p>

    <div class="label__band label__band--bottom"></div>
  </section>
</body>
</html>
```